professional business card design for technology company

We are a small technology consulting firm, specialising in consulting based around Cloud and Managed services. Our colour scheme is yellow, blue and white, as you can see in the logos. Although we are based in melbourne australia, due to the nature of our work, our clients can be located anywhere. We are looking for a clean, professional, positive look - similar to our company logo

Target Market(s)

small business

Industry/Entity Type

Business

Contact Information for Business Card

eye catching, designed to incorporate some level of raised printing. Must contain website address, phone number, name and job title

Requirements
Must have
• Logo (attached) - use of the same colour scheme

```html
<!DOCTYPE html>
<html lang="en">
<head>
<meta charset="utf-8">
<title>Nimbara – Business Card</title>
<link rel="stylesheet" href="https://fonts.googleapis.com/css2?family=Josefin+Sans:wght@400;600;700&display=swap">
<style>
  :root{
    --bg:#e9e7e4;
    --slate:#5e5e5f;
    --sun:#ffd823;
    --brand-blue:#2ba3dc;
    --ink:#5b5b5c;
    --on-slate:#ffffff;
  }
  *{box-sizing:border-box;margin:0;padding:0}
  html,body{width:1200px;height:900px;overflow:hidden}
  body{
    background:var(--bg);
    font-family:"Josefin Sans",sans-serif;
    position:relative;
  }
  .card{
    position:absolute;left:150px;top:193px;width:900px;height:514px;
    border-radius:44px;overflow:hidden;
    box-shadow:0 10px 30px rgba(0,0,0,.18);
  }
  .card-bg{position:absolute;inset:0;width:100%;height:100%}
  .brand{
    position:absolute;left:150px;top:96px;
    display:flex;align-items:center;gap:18px;
  }
  .brand-dot{width:46px;height:46px;border-radius:50%;background:var(--brand-blue)}
  .brand-name{font-size:74px;font-weight:700;color:var(--ink);letter-spacing:-1px;line-height:1}
  .identity{
    position:absolute;right:460px;top:308px;text-align:right;color:var(--on-slate);
    font-variant:small-caps;letter-spacing:2px;
  }
  .identity .person{font-size:26px;font-weight:700;line-height:1.1}
  .identity .role{font-size:21px;margin-top:6px}
  .identity .address{font-size:21px;margin-top:34px;line-height:1.5}
  .divider{position:absolute;left:462px;top:235px;width:2px;height:235px;background:var(--on-slate);opacity:.85}
  .contact{position:absolute;left:486px;top:200px;list-style:none;color:var(--on-slate);
    font-size:21px;letter-spacing:2px;font-variant:small-caps}
  .contact li{display:flex;align-items:center;gap:10px;height:30px}
  .contact li.gap{margin-top:16px}
  .contact svg{width:20px;height:20px;flex:none}
</style>
</head>
<body>
  <section class="card" aria-label="Nimbara business card">
    <svg class="card-bg" viewBox="0 0 900 514" preserveAspectRatio="none" aria-hidden="true">
      <defs>
        <linearGradient id="paper" x1="0" y1="0" x2="0" y2="1">
          <stop offset="0" stop-color="#ffffff"/>
          <stop offset="1" stop-color="#e6e6e6"/>
        </linearGradient>
      </defs>
      <rect width="900" height="514" fill="url(#paper)"/>
      <path d="M0 308 C 240 282, 440 200, 620 150 S 850 88 900 86 L900 514 L0 514 Z" fill="#ffffff"/>
      <path d="M0 314 C 240 290, 440 210, 620 158 S 850 96 900 94 L900 514 L0 514 Z" fill="var(--sun)"/>
      <path d="M0 334 C 250 304, 450 226, 620 174 S 850 108 900 104 L900 514 L0 514 Z" fill="#f4f4f4"/>
      <path d="M0 340 C 250 310, 450 232, 620 180 S 850 112 900 108 L900 514 L0 514 Z" fill="var(--slate)"/>
    </svg>

    <div class="brand">
      <span class="brand-dot"></span>
      <span class="brand-name">Nimbara</span>
    </div>

    <div class="identity">
      <p class="person">Alan Reed</p>
      <p class="role">Owner / C.E.O</p>
      <p class="address">Suite # 418, Kent Hse,<br>VIC 3051</p>
    </div>

    <div class="divider"></div>

    <ul class="contact">
      <li><svg viewBox="0 0 20 20"><circle cx="10" cy="10" r="9" fill="#fff"/><path d="M7 5 l2 3 -1 1 c1 2 2 3 3 3 l1 -1 3 2 -1 2 c-4 0 -8 -4 -8 -8z" fill="var(--slate)"/></svg>555-210-4471</li>
      <li><svg viewBox="0 0 20 20"><circle cx="10" cy="10" r="9" fill="#fff"/><rect x="7" y="4.5" width="6" height="11" rx="1.2" fill="var(--slate)"/></svg>555-318-2290</li>
      <li><svg viewBox="0 0 20 20"><circle cx="10" cy="10" r="9" fill="#fff"/><rect x="5" y="8" width="10" height="6" rx="1" fill="var(--slate)"/><rect x="7" y="5" width="6" height="3" fill="var(--slate)"/></svg>555-604-7713</li>
      <li class="gap"><svg viewBox="0 0 20 20"><circle cx="10" cy="10" r="9" fill="#fff"/><rect x="5" y="6.5" width="10" height="7" fill="var(--slate)"/><path d="M5 6.5 L10 10.5 L15 6.5" stroke="#fff" stroke-width="1" fill="none"/></svg>alan@nimbaracloud.com</li>
      <li><svg viewBox="0 0 20 20"><circle cx="10" cy="10" r="9" fill="#fff"/><circle cx="10" cy="10" r="5.5" fill="none" stroke="var(--slate)" stroke-width="1.2"/><path d="M4.5 10 H15.5 M10 4.5 V15.5" stroke="var(--slate)" stroke-width="1.2"/></svg>www.nimbaracloud.com</li>
    </ul>
  </section>
</body>
</html>
```